Keystone Perks Supplier Statement

We want to design a better look and feel for the attached report. It has to look like the corporate website, match colours and stand out in the eyes of our customers that will receive this report every month. Big numbers and phrase. There has to be a header, nice graphs (you can point the concept we create the graphs with the real numbers) a space for marketing message (banner), space for opportunities (list of top shops) after that shop list details as in the report. www.qorvitel.com for reference. This report is focused on our Loyalty program at www.qorvitel.com/rewards. Use the references for the Loyalty Program.
This design is intended to be converted into a monthly html email statement for our participating Rewards Suppliers.

Target Market(s)

Automotive industry, Automotive OEM Supplier

Industry/Entity Type

Oem Supplier

Font styles to use
Other font styles liked:
• Roboto

Requirements
Must have
• Follow the Corporate Colors from the website and logo. Cannot have anything different than the corporate colours. The Keystone Perks logo shall use the following colors: Color - red (Pantone 485 C) and black (100% Black)
Nice to have
• work with images provided.

```html
<!DOCTYPE html>
<html lang="en">
<head>
<meta charset="utf-8">
<title>Keystone Perks Supplier Statement</title>
<link rel="stylesheet" href="https://fonts.googleapis.com/css2?family=Montserrat:wght@300;400;600;700;800&family=Roboto:wght@400;500;700&display=swap">
<style>
:root{
  --brand-red:#d81f37;
  --ink:#1f1f1f;
  --charcoal:#2a2a2a;
  --black:#0d0d0d;
  --paper:#ffffff;
  --stage:#e7e5e1;
  --row-a:#e9e9e9;
  --row-b:#dcdcdc;
  --panel:#f1f1f1;
  --muted:#555555;
  --peach:#f7d9c6;
  --peach-line:#e39a78;
}
*{box-sizing:border-box;margin:0;padding:0}
html,body{width:1200px;height:2296px;overflow:hidden}
body{background:var(--stage);font-family:"Roboto",Arial,sans-serif;color:var(--ink);position:relative}
.sheet{position:absolute;left:40px;top:357px;width:1120px;height:1582px;background:var(--paper);box-shadow:0 6px 24px rgba(0,0,0,.18);overflow:hidden}
.brand{position:absolute;display:flex;align-items:center;gap:16px}
.brand-mark{width:88px;height:88px;border-radius:50%;background:var(--brand-red);flex:none}
.brand-name{font-family:"Montserrat",Arial,sans-serif;font-weight:800;color:var(--black);line-height:.95;letter-spacing:1px}
.brand-name small{display:block;font-size:.42em;letter-spacing:4px}
.brand--header{left:50%;top:46px;transform:translateX(-50%)}
.brand--header .brand-name{font-size:40px}
.photo{position:absolute}
.photo--climate{left:0;top:175px;width:562px;height:273px;background:linear-gradient(135deg,#3b3d40,#8c8f93 45%,#2b2c2e)}
.photo--clock{left:569px;top:175px;width:278px;height:273px;background:radial-gradient(circle at 50% 50%,#f4f4f4 0 45%,#c9c9c9 47%,#d7374a 60%,#e7e7e7 80%)}
.photo--brakes{left:853px;top:175px;width:267px;height:273px;background:linear-gradient(160deg,#8a8d90,#cfd2d4 40%,#c6283a 62%,#5d6063)}
.photo--pool{left:853px;top:455px;width:267px;height:234px;background:linear-gradient(180deg,#bcd6ea 0,#e9f1f7 45%,#5cb5d8 62%,#d9c9b2 80%,#efe9df)}
.title-band{position:absolute;left:0;top:455px;width:847px;height:234px;background:var(--charcoal);display:flex;align-items:center;padding-left:70px}
.title-band h1{font-family:"Montserrat",Arial,sans-serif;font-weight:400;color:#fff;font-size:34px;letter-spacing:.5px}
.section-title{position:absolute;left:0;width:100%;top:738px;text-align:center;font-family:"Montserrat",Arial,sans-serif;font-weight:700;font-size:21px;color:var(--brand-red)}
.activity{position:absolute;left:79px;top:783px;width:962px;border-collapse:separate;border-spacing:0;border-radius:14px;overflow:hidden;box-shadow:0 4px 8px rgba(0,0,0,.18);font-size:15px}
.activity th{background:var(--black);color:#fff;height:50px;font-weight:700;font-size:16px;border-left:1px solid #333}
.activity th:first-child{text-align:left;padding-left:18px;width:195px;border-left:none}
.activity td{height:61px;text-align:center;font-weight:700;color:var(--ink);border-left:1px solid #fff}
.activity td:first-child{text-align:left;padding-left:18px;border-left:none;font-size:14px}
.activity tbody tr:nth-child(odd) td{background:var(--row-a)}
.activity tbody tr:nth-child(even) td{background:var(--row-b)}
.chart-card{position:absolute;top:1083px;width:457px;height:308px;background:var(--panel);border-radius:20px;box-shadow:0 4px 10px rgba(0,0,0,.2)}
.chart-card--bars{left:79px}
.chart-card--trend{left:584px}
.chart-card svg{position:absolute;left:0;top:0}
.footer{position:absolute;left:0;top:1461px;width:1120px;height:121px;background:var(--black)}
.footer svg{position:absolute;left:0;top:0}
.contact{position:absolute;left:70px;top:38px;color:#fff;font-family:"Montserrat",Arial,sans-serif}
.contact-lead{font-size:15px;letter-spacing:.5px}
.contact-line{font-size:23px;margin-top:4px}
.contact-line strong{font-weight:700}
.brand--footer{left:680px;top:30px;gap:12px}
.brand--footer .brand-mark{width:60px;height:60px}
.brand--footer .brand-name{font-size:27px;color:#fff}
.site{position:absolute;left:963px;top:48px;padding-left:18px;border-left:3px solid #fff;color:#fff;font-family:"Montserrat",Arial,sans-serif;font-weight:700;font-size:17px;line-height:26px}
</style>
</head>
<body>
<main class="sheet">
  <header class="brand brand--header">
    <span class="brand-mark"></span>
    <span class="brand-name">QORVITEL<small>PARTS SOLUTIONS</small></span>
  </header>

  <div class="photo photo--climate" role="img" aria-label="Close-up of car climate control dials"></div>
  <div class="photo photo--clock" role="img" aria-label="Wall clock in front of a calendar"></div>
  <div class="photo photo--brakes" role="img" aria-label="Disc brake with red caliper"></div>
  <div class="title-band"><h1>REWARDS SUPPLIER POINTS STATEMENT</h1></div>
  <div class="photo photo--pool" role="img" aria-label="Sun lounger beside a pool by the sea"></div>

  <h2 class="section-title">:: SHOP ACTIVITY SUMMARY ::</h2>
  <table class="activity">
    <thead>
      <tr><th>COLUMN1</th><th>Jan</th><th>Feb</th><th>Mar</th><th>Apr</th><th>May</th><th>Jun</th><th>Jul</th><th>Aug</th><th>Sep</th><th>Oct</th><th>Nov</th><th>Dec</th></tr>
    </thead>
    <tbody>
      <tr><td>Shops enrolled</td><td>200</td><td>500</td><td>500</td><td>300</td><td>500</td><td>500</td><td>500</td><td>500</td><td>500</td><td>500</td><td>500</td><td>500</td></tr>
      <tr><td>Shops Receiving Pts</td><td>100</td><td>304</td><td>304</td><td>100</td><td>304</td><td>304</td><td>304</td><td>304</td><td>304</td><td>304</td><td>304</td><td>304</td></tr>
      <tr><td>Shops you assinged Pts</td><td>15</td><td>---</td><td>---</td><td>15</td><td>17</td><td>---</td><td>---</td><td>---</td><td>---</td><td>---</td><td>---</td><td>---</td></tr>
    </tbody>
  </table>

  <section class="chart-card chart-card--bars">
    <svg width="457" height="308" viewBox="0 0 457 308" font-family="Roboto, Arial, sans-serif">
      <text x="24" y="80" font-size="11" fill="#444">Shops you assigned Pts</text>
      <rect x="24" y="96" width="9" height="14" fill="#2a2a2a"/>
      <text x="38" y="108" font-size="10" fill="#222">15</text>
      <text x="24" y="137" font-size="11" fill="#444">Shops enrolled</text>
      <rect x="24" y="148" width="164" height="14" fill="#2a2a2a"/>
      <text x="193" y="160" font-size="10" fill="#222">100</text>
      <rect x="24" y="199" width="333" height="14" fill="#d81f37"/>
      <text x="362" y="211" font-size="10" fill="#222">200</text>
      <line x1="24" y1="70" x2="24" y2="222" stroke="#999"/>
      <line x1="24" y1="222" x2="430" y2="222" stroke="#bbb"/>
      <g font-size="9" fill="#555" text-anchor="middle">
        <text x="24" y="238">0%</text><text x="103" y="238">5000%</text><text x="183" y="238">10000%</text><text x="263" y="238">15000%</text><text x="343" y="238">20000%</text><text x="420" y="238">25000%</text>
      </g>
    </svg>
  </section>

  <section class="chart-card chart-card--trend">
    <svg width="457" height="308" viewBox="0 0 457 308" font-family="Roboto, Arial, sans-serif">
      <text x="228" y="84" font-size="13" font-weight="700" text-anchor="middle" fill="#222">Shop Receiving &amp; Redeeming Points</text>
      <g font-size="8" fill="#555">
        <circle cx="90" cy="100" r="3" fill="#2a2a2a"/><text x="96" y="103">Shops you assigned Pts</text>
        <circle cx="205" cy="100" r="3" fill="#e39a78"/><text x="211" y="103">Shops Receiving Pts</text>
        <circle cx="310" cy="100" r="3" fill="#d81f37"/><text x="316" y="103">Shops enrolled</text>
      </g>
      <line x1="33" y1="150" x2="33" y2="247" stroke="#bbb"/>
      <line x1="427" y1="150" x2="427" y2="247" stroke="#bbb"/>
      <line x1="33" y1="247" x2="427" y2="247" stroke="#bbb"/>
      <path d="M33 225 L55 160 L95 160 L118 203 L133 214 L158 168 L427 168 L427 247 L33 247 Z" fill="#f7d9c6"/>
      <path d="M33 225 L55 160 L95 160 L118 203 L133 214 L158 168 L427 168" fill="none" stroke="#e39a78" stroke-width="2"/>
      <path d="M33 235 L55 175 L95 175 L118 212 L133 220 L158 182 L427 182" fill="none" stroke="#d81f37" stroke-width="1" stroke-dasharray="3 3"/>
      <g font-size="7" fill="#666" text-anchor="middle">
        <text x="33" y="260">Jan</text><text x="69" y="260">Feb</text><text x="105" y="260">Mar</text><text x="140" y="260">Apr</text><text x="176" y="260">May</text><text x="212" y="260">Jun</text><text x="248" y="260">Jul</text><text x="284" y="260">Aug</text><text x="320" y="260">Sep</text><text x="356" y="260">Oct</text><text x="391" y="260">Nov</text><text x="427" y="260">Dec</text>
      </g>
    </svg>
  </section>

  <footer class="footer">
    <svg width="1120" height="121" viewBox="0 0 1120 121">
      <polygon points="627,121 645,121 679,0 661,0" fill="#ffffff"/>
    </svg>
    <div class="contact">
      <p class="contact-lead">TO LEARN MORE</p>
      <p class="contact-line"><strong>1.800.555.0142</strong> OR SALES@QORVITEL.COM</p>
    </div>
    <div class="brand brand--footer">
      <span class="brand-mark"></span>
      <span class="brand-name">QORVITEL<small>PARTS SOLUTIONS</small></span>
    </div>
    <div class="site">QORVITEL.COM</div>
  </footer>
</main>
</body>
</html>
```